Life Coaching Business Card

Please check out my website at www.lorettavanmeer.example. Ideally I would like to use the same colors that I used on the site to match my business cards i.e: pink, green, teal, white
I want the final design to include a picture of me and also to be appealing and eye catching. For the picture I submitted, you can crop it smaller to just have my face (exclude my chest) showing.
Industry/Entity Type
Business
Contact Information for Business Card
Loretta Vanmeer
Transformational Life Coach
web: www.lorettavanmeer.example
email: loretta@lorettavanmeer.example
Phone: 555-318-4072
Look and feel
Each slider illustrates characteristics of the customer's brand and the style your logo design should communicate.

```html
<!DOCTYPE html>
<html lang="en">
<head>
<meta charset="utf-8">
<title>Loretta Vanmeer – Business Card</title>
<link rel="stylesheet" href="https://fonts.googleapis.com/css2?family=Mulish:wght@400;700;800&display=swap">
<style>
  :root {
    --pink: #ee1c7a;
    --teal: #1cb8c8;
    --green: #8cc63f;
    --ink: #5a5a5a;
    --white: #ffffff;
    --band: #ededed;
    --stage: #e4e4e4;
  }
  * { margin: 0; padding: 0; box-sizing: border-box; }
  html, body { width: 1200px; height: 1000px; overflow: hidden; }
  body {
    background: var(--stage);
    font-family: "Mulish", sans-serif;
    position: relative;
  }
  .card {
    position: absolute;
    left: 250px;
    width: 700px;
    height: 400px;
    background: var(--white);
    box-shadow: 0 2px 10px rgba(0,0,0,0.12);
    overflow: hidden;
  }
  .card-front { top: 70px; }
  .card-back { top: 530px; }

  .frame-band {
    position: absolute;
    inset: 0;
    background: var(--band);
  }
  .front-inner {
    position: absolute;
    inset: 26px;
    background: var(--white);
  }
  .portrait {
    position: absolute;
    left: 44px;
    top: 44px;
    width: 252px;
    height: 312px;
    background: linear-gradient(160deg, #9a9a9a 0%, #4a4a4a 45%, #d8d8d8 100%);
  }
  .details {
    position: absolute;
    left: 322px;
    top: 56px;
    right: 36px;
    bottom: 44px;
    display: flex;
    flex-direction: column;
  }
  .name {
    color: var(--pink);
    font-weight: 800;
    font-size: 25px;
    letter-spacing: 0.2px;
  }
  .title {
    color: var(--teal);
    font-weight: 400;
    font-size: 44px;
    line-height: 1.1;
    margin-top: 10px;
  }
  .contact {
    margin-top: auto;
    display: grid;
    grid-template-columns: auto 1fr;
    column-gap: 6px;
    row-gap: 2px;
    font-size: 16.5px;
  }
  .contact dt { color: var(--green); text-align: right; }
  .contact dd { color: var(--ink); white-space: nowrap; }

  .back-surface {
    position: absolute;
    inset: 0;
    background: linear-gradient(135deg, #f4f4f4 0%, #eaeaea 100%);
  }
  .name-tag {
    position: absolute;
    left: 50%;
    top: 50%;
    transform: translate(-50%, -50%);
    background: var(--pink);
    color: var(--white);
    font-weight: 800;
    font-size: 24px;
    padding: 12px 26px;
    border-radius: 6px;
    white-space: nowrap;
  }
</style>
</head>
<body>
  <section class="card card-front">
    <div class="frame-band" role="img" aria-label="Light grey diagonal-striped border"></div>
    <div class="front-inner"></div>
    <div class="portrait" role="img" aria-label="Black and white portrait photo of Loretta Vanmeer"></div>
    <div class="details">
      <p class="name">Loretta Vanmeer</p>
      <h1 class="title">Transformational<br>Life Coach</h1>
      <dl class="contact">
        <dt>web:</dt><dd>www.lorettavanmeer.example</dd>
        <dt>email:</dt><dd>loretta@lorettavanmeer.example</dd>
        <dt>phone:</dt><dd>555-318-4072</dd>
      </dl>
    </div>
  </section>

  <section class="card card-back">
    <div class="back-surface" role="img" aria-label="Light grey diagonal-striped background"></div>
    <p class="name-tag">Loretta Vanmeer</p>
  </section>
</body>
</html>
```